Veltrano - Mechanic/Collision Center Business Card

We're looking for a business card design for our mechanic/ collision repair shop.

Can be with colours or monochromatic.

See the attached files.

Many thanks

```html
<!DOCTYPE html>
<html lang="en">
<head>
<meta charset="utf-8">
<title>Veltrano – Business Card</title>
<link rel="stylesheet" href="https://fonts.googleapis.com/css2?family=Roboto:ital,wght@0,900;1,700&display=swap">
<style>
  :root {
    --card-bg: #ffffff;
    --band-grey: #77787b;
    --ink-dark: #1b1f21;
    --brand-blue: #1d9fd9;
    --ghost: #f1f1f1;
    --text-light: #ffffff;
  }
  * { margin: 0; padding: 0; box-sizing: border-box; }
  html, body {
    width: 1200px;
    height: 686px;
    overflow: hidden;
    background: var(--card-bg);
  }
  .card {
    position: relative;
    width: 1200px;
    height: 686px;
    background: var(--card-bg);
    overflow: hidden;
    font-family: "Roboto", Arial, sans-serif;
  }
  .card-shapes {
    position: absolute;
    inset: 0;
    width: 1200px;
    height: 686px;
  }
  .ghost-name {
    position: absolute;
    left: -40px;
    right: -40px;
    top: 530px;
    text-align: center;
    font-weight: 900;
    font-size: 235px;
    line-height: 1;
    letter-spacing: 6px;
    color: var(--ghost);
    text-transform: uppercase;
    white-space: nowrap;
  }
  .brand-mark {
    position: absolute;
    left: 0;
    right: 0;
    top: 170px;
    display: flex;
    flex-direction: column;
    align-items: center;
  }
  .brand-dot {
    width: 190px;
    height: 190px;
    border-radius: 50%;
    background: var(--brand-blue);
  }
  .brand-word {
    margin-top: 20px;
    font-weight: 900;
    font-size: 124px;
    line-height: 1;
    letter-spacing: 10px;
    color: var(--ink-dark);
    text-transform: uppercase;
    white-space: nowrap;
  }
  .company-line {
    position: absolute;
    left: 223px;
    width: 737px;
    top: 594px;
    height: 92px;
    display: flex;
    align-items: center;
    justify-content: center;
    font-style: italic;
    font-weight: 700;
    font-size: 56px;
    color: var(--text-light);
    letter-spacing: 1px;
  }
</style>
</head>
<body>
  <div class="card">
    <div class="ghost-name" aria-hidden="true">Veltrano</div>

    <svg class="card-shapes" viewBox="0 0 1200 686" aria-hidden="true">
      <polygon class="top-band" points="89,0 1143,0 1097,91 137,91" fill="var(--band-grey)"/>
      <polygon class="corner-left" points="0,643 198,643 223,686 0,686" fill="var(--ink-dark)"/>
      <polygon class="corner-right" points="985,643 1200,643 1200,686 960,686" fill="var(--ink-dark)"/>
      <polygon class="name-band" points="257,594 926,594 960,686 223,686" fill="var(--brand-blue)"/>
    </svg>

    <div class="brand-mark">
      <span class="brand-dot"></span>
      <span class="brand-word">Veltrano</span>
    </div>

    <div class="company-line">Veltrano, LDA</div>
  </div>
</body>
</html>
```